Business card and company stationary - Corvane Cleaning Ltd

1. Who are we and who are our customers?

o We are a relatively new cleaning company, established December 2008. We are a small company. We have 24 staff and we offer domestic and commercial cleaning services.
o We both (me and my wife) have been working for many years in the cleaning industry. We worked for some of the biggest and best cleaning companies in UK. We’ve been operatives, supervisors and managers.
o Inevitably after so many years of working for someone else, we decided to start our own business.
o Our domestic customers are middle class families and busy professionals. We’ve got some commercial customers, mainly offices.
o We are growing steadily.

2. What do we do? What are our services?

o Cleaning. We’ve got range of services - not to many but still can be daunting and confusing for some.
o Generally we’ve got domestic and commercial clients. The approach to the domestic cleaning customers is different to the commercial. In the way we want to say that it is cleaning that we do, but we acknowledge the environment and we appreciate the personal circumstances and requirements that are present. We do care, we listen and we try to work out the best possible way to complete our work.
o Mainly we get our work through referrals

3. What do we want with our stationery ?

o To place and maintain our message and reach out to people and organisations
o We want to advertise, communicate and sale.
o We are going to sell services.
o Increase membership, loyalty and support.

We are after business card design, headed letter and compliment slip.
We would like the headed letter to be created in formats suitable for :
- printing format
- also for use in our daily correspondence via e mail with clients and staff in a easy to edit and write format

The website we have is still under contraction and the domain is corvanecleaning.example

Target Market(s)

Families, individuals, businesses.

Industry/Entity Type

Cleaning Service

Contact Information for Business Card

FRONT :
Company Name - Corvane Cleaning Ltd
Company address - 41 Pelbury Rd, Pelbury, Essex, RM14 7QT
Name - Mrs. Teodora Vasilkova - Tedi
Title - Managing Director
Company phone - 020 8837 2591
E mail - tedi.vasilkova@corvanecleaning.example

BACK :

Company website - corvanecleaning.example
E mail - enquiries@corvanecleaning.example

Font styles to use
Serif

Requirements
Must have
• The above items and company logo...maybe at the back. But I'm free for any suggestions.

```html
<!DOCTYPE html>
<html lang="en">
<head>
<meta charset="utf-8">
<title>Corvane Cleaning Ltd — Stationery</title>
<link rel="stylesheet" href="https://fonts.googleapis.com/css2?family=Didact+Gothic&display=swap">
<style>
  :root {
    --bg: #dcdddf;
    --paper: #ffffff;
    --blue: #3ec3ef;
    --ink: #111111;
    --text: #333333;
    --faint: #eeeff1;
    --font: "Didact Gothic", "Century Gothic", sans-serif;
  }
  * { box-sizing: border-box; margin: 0; padding: 0; }
  html, body { width: 1200px; height: 813px; overflow: hidden; }
  body { background: var(--bg); font-family: var(--font); color: var(--text); position: relative; }

  .sheet { position: absolute; background: var(--paper); box-shadow: 0 3px 10px rgba(0,0,0,.12); overflow: hidden; }

  .brand { display: flex; align-items: center; gap: 6px; }
  .brand-mark { border: 2px solid var(--blue); border-radius: 50%; flex: none; }
  .brand-name { color: var(--blue); font-size: 11px; line-height: 1.15; letter-spacing: .5px; text-transform: uppercase; white-space: nowrap; }

  .contact { font-size: 6.5px; line-height: 1.55; color: var(--text); }
  .contact dt { display: inline-block; width: 34px; }
  .contact dd { display: inline; }
  .contact .row { white-space: nowrap; }
  .contact .person { font-size: 7.5px; color: var(--ink); margin-bottom: 1px; white-space: nowrap; }

  .stripes { position: absolute; top: 0; bottom: 0; display: flex; }
  .stripe { height: 100%; }
  .stripe.blue { background: var(--blue); }
  .stripe.black { background: var(--ink); }
  .stripe.gap { background: transparent; }

  /* Compliment slip */
  .slip { left: 24px; top: 320px; width: 344px; height: 162px; }
  .slip .stripes { left: 12px; }
  .slip .brand { position: absolute; right: 16px; top: 14px; }
  .slip .contact { position: absolute; right: 14px; top: 50px; }
  .slip-greeting { position: absolute; left: 92px; bottom: 14px; font-size: 25px; color: var(--ink); letter-spacing: -.3px; }
  .slip-greeting span { color: var(--blue); }

  /* Letterhead */
  .letterhead { left: 396px; top: 48px; width: 496px; height: 700px; }
  .letterhead .stripes { left: 10px; }
  .letterhead .brand { position: absolute; right: 28px; top: 30px; }
  .letterhead .contact { position: absolute; right: 14px; top: 70px; }
  .letterhead-circle { position: absolute; left: 90px; top: 360px; width: 260px; height: 260px; border: 14px solid var(--faint); border-radius: 50%; }

  /* Business cards */
  .card { left: 912px; width: 264px; height: 160px; }
  .card-front { top: 130px; }
  .card-back { top: 360px; }
  .card-front .brand { position: absolute; left: 14px; top: 18px; gap: 5px; }
  .card-front .brand-name { font-size: 8px; letter-spacing: .3px; }
  .card-front .stripes { left: 30px; top: 64px; bottom: 18px; }
  .card-front .contact { position: absolute; right: 9px; top: 20px; font-size: 5.8px; }
  .card-front .contact dt { width: 29px; }
  .card-front .contact .person { font-size: 7px; }
  .card-back .stripes { left: 10px; }
  .card-back .brand { position: absolute; left: 70px; top: 44px; }
  .card-back .tagline { position: absolute; left: 56px; right: 12px; top: 92px; font-size: 7px; text-align: center; color: var(--text); }
  .card-back .web { position: absolute; left: 56px; right: 12px; top: 108px; font-size: 6.5px; text-align: center; line-height: 1.6; }
</style>
</head>
<body>

  <section class="sheet slip" aria-label="Compliment slip">
    <div class="stripes">
      <div class="stripe blue" style="width:5px"></div><div class="stripe gap" style="width:4px"></div>
      <div class="stripe black" style="width:6px"></div><div class="stripe gap" style="width:4px"></div>
      <div class="stripe blue" style="width:5px"></div><div class="stripe gap" style="width:3px"></div>
      <div class="stripe black" style="width:10px"></div><div class="stripe gap" style="width:4px"></div>
      <div class="stripe blue" style="width:6px"></div><div class="stripe gap" style="width:3px"></div>
      <div class="stripe black" style="width:3px"></div><div class="stripe gap" style="width:4px"></div>
      <div class="stripe blue" style="width:14px"></div>
    </div>
    <div class="brand"><span class="brand-mark" style="width:26px;height:26px"></span><span class="brand-name">Corvane<br>Cleaning Ltd</span></div>
    <dl class="contact">
      <div class="person">Mrs. Teodora Vasilkova - Tedi</div>
      <div class="row"><dt>Office</dt><dd>020 8837 2591</dd></div>
      <div class="row"><dt>Email</dt><dd>enquiries@corvanecleaning.example</dd></div>
      <div class="row"><dt>Address</dt><dd>41 Pelbury Rd, Pelbury, Essex, RM14 7QT</dd></div>
      <div class="row"><dt>Web</dt><dd>corvanecleaning.example</dd></div>
    </dl>
    <p class="slip-greeting">With<span>Compliments!</span></p>
  </section>

  <section class="sheet letterhead" aria-label="Headed letter">
    <div class="stripes">
      <div class="stripe black" style="width:7px"></div><div class="stripe gap" style="width:6px"></div>
      <div class="stripe blue" style="width:3px"></div>
    </div>
    <div class="letterhead-circle" aria-hidden="true"></div>
    <div class="brand"><span class="brand-mark" style="width:28px;height:28px"></span><span class="brand-name">Corvane<br>Cleaning Ltd</span></div>
    <dl class="contact">
      <div class="person">Mrs. Teodora Vasilkova - Tedi</div>
      <div class="row"><dt>Position</dt><dd>Managing Director</dd></div>
      <div class="row"><dt>Office</dt><dd>020 8837 2591</dd></div>
      <div class="row"><dt>Email</dt><dd>tedi.vasilkova@corvanecleaning.example</dd></div>
      <div class="row"><dt>Address</dt><dd>41 Pelbury Rd, Pelbury, Essex, RM14 7QT</dd></div>
      <div class="row"><dt>Web</dt><dd>corvanecleaning.example</dd></div>
    </dl>
  </section>

  <section class="sheet card card-front" aria-label="Business card front">
    <div class="brand"><span class="brand-mark" style="width:20px;height:20px"></span><span class="brand-name">Corvane<br>Cleaning Ltd</span></div>
    <div class="stripes">
      <div class="stripe blue" style="width:6px"></div><div class="stripe gap" style="width:4px"></div>
      <div class="stripe black" style="width:8px"></div><div class="stripe gap" style="width:3px"></div>
      <div class="stripe blue" style="width:5px"></div><div class="stripe gap" style="width:4px"></div>
      <div class="stripe black" style="width:3px"></div><div class="stripe gap" style="width:3px"></div>
      <div class="stripe blue" style="width:16px"></div>
    </div>
    <dl class="contact">
      <div class="person">Mrs. Teodora Vasilkova - Tedi</div>
      <div class="row"><dt>Position</dt><dd>Managing Director</dd></div>
      <div class="row"><dt>Office</dt><dd>020 8837 2591</dd></div>
      <div class="row"><dt>Email</dt><dd>tedi.vasilkova@corvanecleaning.example</dd></div>
      <div class="row"><dt>Address</dt><dd>41 Pelbury Rd, Pelbury, Essex, RM14 7QT</dd></div>
    </dl>
  </section>

  <section class="sheet card card-back" aria-label="Business card back">
    <div class="stripes">
      <div class="stripe blue" style="width:5px"></div><div class="stripe gap" style="width:3px"></div>
      <div class="stripe black" style="width:6px"></div><div class="stripe gap" style="width:3px"></div>
      <div class="stripe blue" style="width:4px"></div>
    </div>
    <div class="brand"><span class="brand-mark" style="width:30px;height:30px"></span><span class="brand-name">Corvane<br>Cleaning Ltd</span></div>
    <p class="tagline">Caring cleaning for homes and offices</p>
    <p class="web">corvanecleaning.example<br>enquiries@corvanecleaning.example</p>
  </section>

</body>
</html>
```